依頼詳細
開設告知を病院や行政、居宅介護支援事業所に行うための簡易的なチラシの作成をお願いいたします。情報量は最低限で、雰囲気重視、まずは時期と場所をしっかりと伝えて初期段階の営業を行うためのツールを想定しています。
記載項目
別紙資料をご確認ください。
サイズ
A4
ページ数
片面
希望イメージ
シンプル 複雑
単色 カラフル
暗い 明るい
日常 高級
遊び心 厳粛
未来的 伝統的
女性的 男性的
希望する色
納品ファイル
補足説明

スタッフの投票で決めました。

大変すばらしい提案をいただきましてありがとうございました。今後もパンフレット等、様々依頼をさせていただく予定ですので、今後とも宜しくお願い致します。

```html
<!DOCTYPE html>
<html lang="ja">
<head>
<meta charset="utf-8">
<title>住宅型有料老人ホーム つきあかり 月灯 開設のご案内</title>
<link rel="stylesheet" href="https://fonts.googleapis.com/css2?family=Zen+Maru+Gothic:wght@500;700;900&family=Noto+Serif+JP:wght@700;900&display=swap">
<style>
:root{
  --navy:#1d2c6a;
  --blue:#2f7fd0;
  --sky:#d9ecf8;
  --pink:#e0336f;
  --purple:#6a4f9e;
  --leaf:#4f8a3a;
  --leaf-dark:#2f5f2a;
  --iris:#8c6fc4;
  --paper:#ffffff;
  --text:#222;
}
*{margin:0;padding:0;box-sizing:border-box}
html,body{width:848px;height:1200px;overflow:hidden}
body{font-family:"Zen Maru Gothic",sans-serif;color:var(--text);background:#fff}
.flyer{position:relative;width:848px;height:1200px;overflow:hidden}
.scenery{position:absolute;inset:0;background:
  linear-gradient(180deg,#7fb35f 0%,#4f8a3a 30%,#3d6f34 45%,#6e9a4a 60%,#8c6fc4 78%,#5e7f3c 100%);}
.sky-glow{position:absolute;left:120px;top:0;width:608px;height:330px;
  background:radial-gradient(ellipse at 50% 40%,rgba(255,255,255,.97) 0%,rgba(255,255,255,.9) 45%,rgba(255,255,255,0) 72%);}
.brand{position:absolute;left:0;right:0;top:24px;text-align:center;color:var(--navy)}
.brand-mark{display:block;margin:0 auto 12px;width:120px;height:120px}
.brand-type{font-size:28px;font-weight:700;letter-spacing:.06em}
.brand-name{font-size:78px;font-weight:900;line-height:1.05;letter-spacing:.08em}
.brand-kanji{font-size:38px;font-weight:700;letter-spacing:.5em;margin-left:.5em}
.opening{position:absolute;left:0;right:0;top:325px;height:64px;background:var(--navy);
  color:#fff;text-align:center;font-family:"Noto Serif JP",serif;font-weight:900;font-size:46px;line-height:64px;letter-spacing:.06em}
.features{position:absolute;left:26px;top:410px;width:392px;height:650px;background:rgba(255,255,255,.93);padding:22px 22px}
.features h2{text-align:center;color:var(--pink);font-size:24px;font-weight:900;margin-bottom:14px}
.features h2 span{color:var(--navy)}
.feature-list{list-style:none;font-size:16px;line-height:1.55;font-weight:500}
.feature-list li{position:relative;padding-left:22px;margin-bottom:8px}
.feature-list li::before{content:"";position:absolute;left:2px;top:7px;width:12px;height:12px;background:var(--blue);border-radius:50%}
.fee-table{width:100%;margin-top:16px;border-collapse:separate;border-spacing:0 6px;font-size:22px;font-weight:900}
.fee-table th{width:110px;background:var(--purple);color:#fff;font-weight:700;text-align:center;letter-spacing:.4em;padding:3px 0 3px .4em}
.fee-table td{color:var(--navy);padding-left:22px}
.fee-table tr.total th{background:var(--pink)}
.fee-note{font-size:13px;color:#444;margin-top:4px}
.services{position:absolute;left:500px;top:410px;width:320px;height:110px;background:var(--paper);padding:14px 16px;color:var(--pink);font-weight:900}
.services .line{display:block;font-size:29px;line-height:1.25;background:var(--pink);color:#fff;padding:0 8px;margin-bottom:6px;width:236px}
.services .badge{position:absolute;right:10px;top:30px;font-size:30px;writing-mode:vertical-rl;color:var(--navy)}
.access{position:absolute;left:440px;top:545px;width:382px;height:360px;background:var(--paper);padding:12px}
.access-head{display:flex;align-items:center;gap:8px;color:var(--navy);font-weight:900;font-size:20px;margin-bottom:8px}
.access-head i{width:16px;height:16px;background:var(--blue);border-radius:50%;display:block}
.map{height:268px;background:linear-gradient(135deg,#eef4f9,#cfe3f3)}
.address{font-size:13px;margin-top:8px;text-align:right;font-weight:700}
.contact{position:absolute;left:0;right:0;bottom:0;height:112px;background:var(--navy);color:#fff;text-align:center;padding-top:10px}
.contact-label{font-size:26px;font-weight:900;letter-spacing:.1em}
.contact-tel{font-size:50px;font-weight:900;line-height:1.2;letter-spacing:.04em}
.contact-tel small{font-size:26px;letter-spacing:0}
</style>
</head>
<body>
<main class="flyer">
  <div class="scenery" role="img" aria-label="新緑の木々と紫色の花菖蒲が咲く公園の風景写真"></div>
  <div class="sky-glow"></div>

  <header class="brand">
    <svg class="brand-mark" viewBox="0 0 120 120" aria-hidden="true"><circle cx="60" cy="60" r="52" fill="var(--blue)"/></svg>
    <p class="brand-type">住宅型有料老人ホーム</p>
    <h1 class="brand-name">つきあかり</h1>
    <p class="brand-kanji">月灯</p>
  </header>

  <div class="opening">令和3年4月オープン</div>

  <section class="features">
    <h2><span>“つきあかり”</span>4つの特色</h2>
    <ul class="feature-list">
      <li>みずべ沼ふれあい公園徒歩1分。自然豊かで落ち着いたホームです。</li>
      <li>理学療法士、作業療法士を配置し、機能維持と機能改善に力を入れています。毎日の暮らしを楽しんでいただけます。</li>
      <li>シアタールーム等、余暇設備が充実しています。</li>
      <li>畑・園芸スペースもあります。季節の草花や野菜の栽培を楽しみましょう。</li>
    </ul>
    <table class="fee-table">
      <tr><th>家賃</th><td>27,000円〜</td></tr>
      <tr><th>食費</th><td>39,000円</td></tr>
      <tr><th>管理費</th><td>18,000円</td></tr>
      <tr class="total"><th>合計</th><td>84,000円〜</td></tr>
    </table>
    <p class="fee-note">※お部屋のタイプによって家賃は異なります。</p>
  </section>

  <aside class="services">
    <span class="line">訪問介護事業所</span>
    <span class="line">通所介護事業所</span>
    <span class="badge">併設!</span>
  </aside>

  <section class="access">
    <div class="access-head"><i></i>つきあかり 月灯</div>
    <div class="map" role="img" aria-label="ホーム周辺の道路とみずべ沼ふれあい公園の位置を示す案内地図"></div>
    <p class="address">住所：○○県△△市みずべ町1234-5</p>
  </section>

  <footer class="contact">
    <p class="contact-label">【お問い合わせ先】</p>
    <p class="contact-tel">000-000-0000<small>（開設準備室）</small></p>
  </footer>
</main>
</body>
</html>
```